Business Card for Pottery and Jewellery Designer

A new business card design is needed to accompany a newly launching pottery and jewellery website. The company logo has been attached for use. The company is called Glazewick Studio. For a sense of the vibe please see the website (it is currently under construction but this way you'll get a feel for the style) www.GlazewickStudio.com

The website font is Pontano Sans for the body of the text with Overlock for headers.

The overall look should be clean and elegant. The back side can have just the logo. The front side should have a smaller logo and the following details displayed:

Glazewick Studio
Designer: Hollis Marrow
Phone: xxx.xxx.xxxx
Email: Designer@GlazewickStudio.com

The structure of displaying this is completely up to you. Different layouts and creative methods of displaying contact info are welcome as long as it stays clean/uncluttered.

No product photographs are to be included in the design as the catalogue changes quickly.

Colour preferences lean towards elegant and understated (charcoal grey, dark navy blue etc.)

Please let me know if you have any further questions or further details required.

Target Market(s)

Target market is 30+ year old women

Industry/Entity Type

Construction

Colors
ffffff
1b1b1b
474747
d9d9d9
fafafa
0355a3

Requirements
Must have
• The submissions so far have looked very typical and don't stand out right now. They're also all in navy with very little variation. I'm looking for something that stands out a it more while still being clean-looking.
Nice to have
• I've attached a few design samples and an idea for a backdrop. It would be great to see some designs in black, white, and grey with only a hint of color.
Should not have
• Product Images

```html
<!DOCTYPE html>
<html lang="en">
<head>
<meta charset="utf-8">
<title>Glazewick Studio – Business Card</title>
<link rel="stylesheet" href="https://fonts.googleapis.com/css2?family=Arimo:wght@400;700&family=Space+Mono:wght@700&display=swap">
<style>
  :root {
    --charcoal: #1b1b1b;
    --graphite: #474747;
    --slate: #6e6e6e;
    --mist: #bdbdbd;
    --pale: #d9d9d9;
    --haze: #ececec;
    --paper: #ffffff;
    --accent: #0355a3;
    --ink: #2b2b2b;
  }
  * { margin: 0; padding: 0; box-sizing: border-box; }
  html, body {
    width: 1200px; height: 329px; overflow: hidden;
    background: var(--paper);
  }
  .sheet { position: relative; width: 1200px; height: 329px; }
  .card { position: absolute; top: 0; height: 329px; overflow: hidden; background: var(--paper); }
  .card--front { left: 0; width: 598px; }
  .card--back { left: 622px; width: 578px; }
  .card__backdrop { position: absolute; inset: 0; }

  .brand-title {
    position: absolute; left: 74px; top: 10px;
    font-family: "Space Mono", monospace; font-weight: 700;
    font-size: 36px; letter-spacing: 4px; line-height: 1.1;
    color: var(--charcoal);
    text-shadow: 1px 1px 0 var(--mist);
    white-space: nowrap;
  }
  .contact {
    position: absolute; left: 119px; top: 82px; list-style: none;
    font-family: "Arimo", Arial, sans-serif; font-size: 17px; line-height: 20px;
    color: var(--ink);
  }
  .contact li { height: 50px; }

  .wordmark {
    position: absolute; display: flex; align-items: center; gap: 10px;
    font-family: "Arimo", Arial, sans-serif; font-weight: 700; color: var(--charcoal);
    white-space: nowrap;
  }
  .wordmark__dot { border-radius: 50%; background: var(--accent); flex: none; }
  .wordmark--small { left: 352px; top: 226px; font-size: 20px; }
  .wordmark--small .wordmark__dot { width: 14px; height: 14px; }
  .wordmark--large { left: 150px; top: 138px; font-size: 40px; }
  .wordmark--large .wordmark__dot { width: 30px; height: 30px; }
</style>
</head>
<body>
<main class="sheet">

  <section class="card card--front" aria-label="Card front">
    <svg class="card__backdrop" viewBox="0 0 598 329" aria-hidden="true">
      <defs>
        <radialGradient id="frontSwoosh" cx="0.05" cy="0.35" r="0.9">
          <stop offset="0" stop-color="#ffffff"/>
          <stop offset="0.45" stop-color="#c4c4c4"/>
          <stop offset="1" stop-color="#474747"/>
        </radialGradient>
        <linearGradient id="frontPool" x1="0" y1="0" x2="1" y2="0">
          <stop offset="0" stop-color="#6e6e6e"/>
          <stop offset="1" stop-color="#1b1b1b"/>
        </linearGradient>
      </defs>
      <path d="M0,40 Q20,230 150,329 L0,329 Z" fill="url(#frontSwoosh)"/>
      <path d="M40,250 Q110,320 240,300 Q420,260 598,275 L598,329 L120,329 Q70,300 40,250 Z" fill="#ececec"/>
      <path d="M130,329 Q300,250 598,262 L598,329 Z" fill="url(#frontPool)"/>
      <path d="M300,329 Q360,225 598,230 L598,262 Q400,255 330,329 Z" fill="#d9d9d9"/>
      <path d="M315,329 Q370,240 598,246" fill="none" stroke="#0355a3" stroke-width="2"/>
    </svg>
    <h1 class="brand-title">Glazewick Studio</h1>
    <ul class="contact">
      <li>Designer:Hollis Marrow</li>
      <li>T: xxx-xxx-xxxx</li>
      <li>E:Designer@GlazewickStudio.com</li>
    </ul>
    <div class="wordmark wordmark--small"><span class="wordmark__dot"></span>Glazewick Studio</div>
  </section>

  <section class="card card--back" aria-label="Card back">
    <svg class="card__backdrop" viewBox="0 0 578 329" aria-hidden="true">
      <defs>
        <linearGradient id="backCorner" x1="0" y1="0" x2="0.3" y2="1">
          <stop offset="0" stop-color="#474747"/>
          <stop offset="0.55" stop-color="#bdbdbd"/>
          <stop offset="1" stop-color="#ffffff"/>
        </linearGradient>
      </defs>
      <path d="M0,0 L578,0 L578,22 Q420,4 270,8 Q130,30 95,150 Q75,250 140,329 L0,329 Z" fill="url(#backCorner)"/>
      <path d="M270,8 Q130,30 95,150 Q75,250 140,329" fill="none" stroke="#d9d9d9" stroke-width="10"/>
      <path d="M283,14 Q145,36 108,150 Q90,245 152,329" fill="none" stroke="#0355a3" stroke-width="2"/>
    </svg>
    <div class="wordmark wordmark--large"><span class="wordmark__dot"></span>Glazewick Studio</div>
  </section>

</main>
</body>
</html>
```